Business Card Design Project

We are a commercial talent casting company, a very "now" company. We need a new business card that is both current, graphic and elegantly interesting. As we are a service business,
we need something that will attract the attention of new clients,
yet project a business that is 25 years old.

Industry/Entity Type

Business

Requirements
Must have
• 1. Logo - Nora Quillan Casting
2. Address - 47 Thornbury Street
New York, New York 10010
3. Phone - 212-738-4192
4. E-Mail - Casting@noraquillan.example

Nice to have
• Would like the card in black and white with the only accent
color being red.

```html
<!DOCTYPE html>
<html lang="en">
<head>
<meta charset="utf-8">
<title>Nora Quillan Casting — Business Card</title>
<link href="https://fonts.googleapis.com/css2?family=Share+Tech+Mono&display=swap" rel="stylesheet">
<style>
  :root {
    --page: #d9d9d9;
    --card: #050505;
    --ink: #f2f2f2;
    --muted: #cfcfcf;
    --accent: #c8141c;
    --hole: #ffffff;
  }
  html, body {
    margin: 0;
    width: 1200px;
    height: 900px;
    overflow: hidden;
    background: var(--page);
    font-family: "Share Tech Mono", "Courier New", monospace;
  }
  .card {
    position: absolute;
    left: 75px;
    top: 150px;
    width: 1050px;
    height: 600px;
    background: var(--card);
    box-shadow: 0 10px 30px rgba(0,0,0,0.35);
    overflow: hidden;
  }
  .film-strip {
    position: absolute;
    left: 0;
    width: 1050px;
    height: 70px;
  }
  .film-strip--top { top: 0; }
  .film-strip--bottom { bottom: 0; }

  .brand {
    position: absolute;
    left: 150px;
    top: 125px;
    display: flex;
    align-items: center;
    gap: 22px;
  }
  .brand__mark {
    width: 40px;
    height: 40px;
    border: 3px solid var(--accent);
    box-sizing: border-box;
  }
  .brand__name {
    color: var(--ink);
    font-size: 50px;
    letter-spacing: 1px;
  }
  .brand__rule {
    position: absolute;
    left: 150px;
    top: 200px;
    width: 560px;
    height: 3px;
    background: var(--accent);
  }

  .person {
    position: absolute;
    left: 80px;
    top: 320px;
  }
  .person__name {
    color: var(--ink);
    font-size: 46px;
    padding-bottom: 6px;
    border-bottom: 2px solid var(--ink);
    display: inline-block;
    padding-right: 40px;
  }
  .person__role {
    color: var(--accent);
    font-size: 26px;
    margin-top: 4px;
    padding-left: 40px;
  }

  .contact {
    position: absolute;
    left: 500px;
    top: 380px;
    padding-left: 26px;
    border-left: 2px solid var(--accent);
    color: var(--muted);
    font-size: 22px;
    font-style: normal;
    line-height: 1.3;
  }
  .contact p { margin: 0; }
  .contact__gap { height: 18px; }
  .contact__label { color: var(--accent); }
</style>
</head>
<body>
  <main class="card" aria-label="Nora Quillan Casting business card">
    <svg class="film-strip film-strip--top" viewBox="0 0 1050 70" aria-hidden="true">
      <defs>
        <pattern id="sprocket" x="0" y="0" width="70" height="70" patternUnits="userSpaceOnUse">
          <rect x="12" y="20" width="46" height="30" rx="8" fill="#ffffff"/>
        </pattern>
      </defs>
      <rect x="0" y="0" width="1050" height="70" fill="url(#sprocket)"/>
    </svg>

    <div class="brand">
      <span class="brand__mark" aria-hidden="true"></span>
      <span class="brand__name">Nora Quillan Casting</span>
    </div>
    <div class="brand__rule" aria-hidden="true"></div>

    <section class="person">
      <div class="person__name">Your Name</div>
      <div class="person__role">owner</div>
    </section>

    <address class="contact">
      <p>47 Thornbury Street</p>
      <p>New York, New York 10010</p>
      <div class="contact__gap"></div>
      <p><span class="contact__label">Phone -</span> 212-738-4192</p>
      <p><span class="contact__label">E-Mail -</span> Casting@noraquillan.example</p>
    </address>

    <svg class="film-strip film-strip--bottom" viewBox="0 0 1050 70" aria-hidden="true">
      <rect x="0" y="0" width="1050" height="70" fill="url(#sprocket)"/>
    </svg>
  </main>
</body>
</html>
```